Website for new crypto research organization

See brief (attached). This is a pretty basic website with only a handful of pages + ability to collect email addresses.

```html
<!DOCTYPE html>
<html lang="en">
<head>
<meta charset="utf-8">
<title>Tidewater Ledger</title>
<link href="https://fonts.googleapis.com/css2?family=Urbanist:wght@400;500;600;700;800&display=swap" rel="stylesheet">
<style>
:root{
  --teal:#00a69c;
  --sky:#1aa7cf;
  --ink:#1c1c1c;
  --muted:#5b5b5b;
  --paper:#f9f9f9;
  --white:#ffffff;
}
*{box-sizing:border-box;margin:0;padding:0}
html,body{width:1200px;height:2730px;overflow:hidden}
body{font-family:"Urbanist",sans-serif;color:var(--ink);background:var(--white)}
.wrap{width:978px;margin:0 auto;position:relative}
.site-header{height:105px}
.site-header .wrap{display:flex;align-items:center;justify-content:space-between;height:105px}
.brand{display:flex;align-items:center;gap:8px;font-weight:700;font-size:20px;color:var(--teal)}
.brand-dot{width:14px;height:14px;background:var(--teal)}
.main-nav{display:flex;gap:41px;font-size:16px;font-weight:500}
.main-nav a{color:var(--ink);text-decoration:none}
.main-nav a.active{color:var(--teal)}
.main-nav .login::before{content:"";display:inline-block;width:9px;height:11px;background:var(--teal);border-radius:5px 5px 1px 1px;margin-right:4px}
.hero{position:relative;height:585px;overflow:hidden}
.hero-art{position:absolute;inset:0;background:linear-gradient(100deg,#9c9c9c 0%,#b4b2ae 30%,#8a6c54 55%,#7b8fa6 75%,#c3a0b6 100%)}
.hero .wrap{padding-top:218px}
.hero h1{font-size:70px;font-weight:800;line-height:78px;letter-spacing:-1px;color:#0b0b0b}
.hero p{width:420px;margin-top:12px;font-size:15px;line-height:27px;font-weight:500;color:#111}
.research{background:var(--paper);height:708px;text-align:center;padding-top:72px}
.section-title{font-size:46px;font-weight:800}
.section-lead{width:560px;margin:16px auto 0;font-size:15px;line-height:26px;color:var(--muted)}
.rule{width:112px;height:4px;background:var(--teal);margin:27px auto 0}
.features{display:flex;justify-content:space-between;margin-top:50px}
.feature{width:310px}
.feature-icon{width:136px;height:136px;border-radius:50%;background:var(--teal);margin:0 auto;display:flex;align-items:center;justify-content:center}
.feature h3{font-size:18px;font-weight:700;margin-top:20px}
.feature p{font-size:14px;line-height:26px;color:var(--muted);margin-top:10px}
.btn{display:inline-block;margin-top:59px;background:var(--teal);color:var(--white);font-size:15px;font-weight:600;width:296px;height:58px;line-height:58px;text-decoration:none}
.recent{background:var(--teal);height:639px;text-align:center;padding-top:62px;color:var(--white)}
.recent .section-lead{color:var(--white);margin-top:8px}
.recent .rule{background:var(--white);margin-top:17px}
.cards{display:flex;gap:13px;margin-top:30px;text-align:left}
.card{width:317px;height:353px;background:var(--white);border-radius:6px;padding:20px 15px;color:var(--ink)}
.card h3{font-size:19px;font-weight:700}
.card time{display:block;font-size:14px;margin-top:10px;color:#333}
.card p{font-size:14px;line-height:27.5px;color:var(--muted);margin-top:22px;padding:0 2px}
.card a{display:inline-block;margin-top:20px;color:var(--teal);font-weight:600;font-size:15px;text-decoration:underline}
.newsletter{height:429px;background:linear-gradient(180deg,#f4f4f4,#fafafa);border-bottom:1px solid #bfe3e0;padding-top:57px}
.sub-box{width:493px;height:310px;margin:0 auto;border:8px solid var(--teal);border-right:3px solid var(--sky);border-bottom-color:var(--sky);text-align:center;padding-top:44px}
.sub-box .mark{font-size:20px;font-weight:700;color:var(--teal)}
.sub-box h2{font-size:34px;font-weight:700;margin-top:12px}
.sub-box .tag{font-size:18px;margin-top:8px}
.sub-form{display:flex;width:384px;margin:34px auto 0;height:52px}
.sub-form input{flex:1;border:1px solid var(--sky);border-right:none;padding-left:16px;font-family:inherit;font-size:15px}
.sub-form button{width:137px;background:var(--sky);color:var(--white);border:none;font-family:inherit;font-size:18px;font-weight:700}
.site-footer{text-align:center;padding-top:76px}
.foot-nav{display:flex;justify-content:center;gap:47px;font-size:19px}
.foot-nav a{color:var(--ink);text-decoration:none}
.social{display:flex;justify-content:center;gap:9px;margin-top:34px}
.social span{width:44px;height:44px;border:1px solid #cfcfcf;border-radius:50%}
.copy{font-size:16px;margin-top:26px}
</style>
</head>
<body>
<header class="site-header">
  <div class="wrap">
    <div class="brand"><span class="brand-dot"></span>Tidewater Ledger</div>
    <nav class="main-nav">
      <a class="active" href="#">Home</a><a href="#">About Us</a><a href="#">Research</a><a href="#">News</a><a href="#">Careers</a><a href="#">Contact</a><a class="login" href="#">Login</a>
    </nav>
  </div>
</header>

<section class="hero">
  <div class="hero-art" role="img" aria-label="Elephant bursting through a graffiti-covered brick wall"></div>
  <div class="wrap">
    <h1>Tidewater<br>Ledger</h1>
    <p>Lorem ipsum dolor sit amet, consectetur adipiscing elit, sed do eiusmod tempor incididunt ut labore et dolore magna aliqua. Ut enim ad minim veniam.</p>
  </div>
</section>

<section class="research">
  <div class="wrap">
    <h2 class="section-title">Research</h2>
    <p class="section-lead">Lorem ipsum dolor sit amet, consectetur adipiscing elit, sed do eiusmod tempor incididunt ut labore et dolore magna aliqua.</p>
    <div class="rule"></div>
    <div class="features">
      <div class="feature">
        <div class="feature-icon">
          <svg width="80" height="80" viewBox="0 0 80 80" fill="none" stroke="#fff" stroke-width="3"><circle cx="40" cy="40" r="12"/><circle cx="40" cy="40" r="24" stroke-dasharray="10 5"/><circle cx="40" cy="40" r="34"/></svg>
        </div>
        <h3>Technical Evaluation</h3>
        <p>Lorem ipsum dolor sit amet, adipiscing elit, sed do eiusmod tempor incididunt ut labore et dolore magna aliqua.</p>
      </div>
      <div class="feature">
        <div class="feature-icon">
          <svg width="80" height="80" viewBox="0 0 80 80" fill="none" stroke="#fff" stroke-width="3"><circle cx="26" cy="26" r="6"/><circle cx="40" cy="22" r="6"/><circle cx="54" cy="26" r="6"/><path d="M16 44h48M10 50h10v20H10zM20 66c14 4 30 0 48-14"/></svg>
        </div>
        <h3>Community Engagement</h3>
        <p>Lorem ipsum dolor sit amet, adipiscing elit, sed do eiusmod tempor incididunt ut labore et dolore magna aliqua.</p>
      </div>
      <div class="feature">
        <div class="feature-icon">
          <svg width="80" height="80" viewBox="0 0 80 80" fill="none" stroke="#fff" stroke-width="3"><rect x="8" y="14" width="52" height="44"/><path d="M16 50V40M24 50V34M32 50V44M30 30l10-8 8 6 14-12"/><circle cx="56" cy="58" r="12" fill="#00a69c"/><circle cx="56" cy="58" r="5"/></svg>
        </div>
        <h3>On-chain data analysis</h3>
        <p>Lorem ipsum dolor sit amet, adipiscing elit, sed do eiusmod tempor incididunt ut labore et dolore magna aliqua.</p>
      </div>
    </div>
    <a class="btn" href="#">RECENT RESEARCH REPORTS</a>
  </div>
</section>

<section class="recent">
  <div class="wrap">
    <h2 class="section-title">Recent Research</h2>
    <p class="section-lead">Lorem ipsum dolor sit amet, consectetur adipiscing elit, sed do eiusmod tempor incididunt ut labore et dolore magna aliqua.</p>
    <div class="rule"></div>
    <div class="cards">
      <article class="card"><h3>Lorem ipsum dolor sit amet,</h3><time>25-01-2022</time><p>Lorem ipsum dolor sit amet, consectetur adipiscing elit, sed do eiusmodincididunt ut labore et dolore magna aliqua. Ut enim ad minim veniam, Lorem ipsum dolor sit amet, consectetur adipiscing elit, sed do eiusmod tempor incididunt</p><a href="#">Read More</a></article>
      <article class="card"><h3>Lorem ipsum dolor sit amet,</h3><time>25-01-2022</time><p>Lorem ipsum dolor sit amet, consectetur adipiscing elit, sed do eiusmodincididunt ut labore et dolore magna aliqua. Ut enim ad minim veniam, Lorem ipsum dolor sit amet, consectetur adipiscing elit, sed do eiusmod tempor incididunt</p><a href="#">Read More</a></article>
      <article class="card"><h3>Lorem ipsum dolor sit amet,</h3><time>25-01-2022</time><p>Lorem ipsum dolor sit amet, consectetur adipiscing elit, sed do eiusmodincididunt ut labore et dolore magna aliqua. Ut enim ad minim veniam, Lorem ipsum dolor sit amet, consectetur adipiscing elit, sed do eiusmod tempor incididunt</p><a href="#">Read More</a></article>
    </div>
  </div>
</section>

<section class="newsletter">
  <div class="sub-box">
    <div class="mark">Tidewater Ledger</div>
    <h2>Newsletter Subscribe</h2>
    <p class="tag">Get more details to signup</p>
    <form class="sub-form"><input type="email" placeholder="Type your email..."><button type="button">Subscribe</button></form>
  </div>
</section>

<footer class="site-footer">
  <nav class="foot-nav"><a href="#">Home</a><a href="#">About Us</a><a href="#">Research</a><a href="#">News</a><a href="#">Careers</a><a href="#">Contact</a></nav>
  <div class="social"><span></span><span></span></div>
  <p class="copy">© 2022 All Rights Reserved</p>
</footer>
</body>
</html>
```